Luxury WordPress Website for CORALBASINS

I need a professional WordPress website for Coral Basins. The site should be modern, visually appealing, and user-friendly, reflecting the brand’s luxury and premium identity. It must include a homepage, product/service pages, contact form, and be responsive on both desktop and mobile devices. The design should allow for easy updates and integration of future content, while maintaining a polished and professional look.

Target Market(s)

swimmingpool & spa

Industry/Entity Type

Swimmingpool

Coding

Coded - Design and coding required

Font styles to use
Other font styles liked:
• HaboroSoft

Requirements
Must have
• Exclusive appearance
Nice to have
• • A logo that subtly incorporates water or pool elements. • A color palette that reflects luxury, elegance, and relaxation. • Clean and modern typography that is easy to read across all media. • Iconography or design elements that convey premium quality. • A versatile design that can be adapted for social media, merchandise, and promotional materials. • Optional: A tagline that emphasizes luxury and high-end pool experiences.

```html
<!DOCTYPE html>
<html lang="en">
<head>
<meta charset="utf-8">
<title>Coral Basins – Luxury Pools</title>
<link rel="stylesheet" href="https://fonts.googleapis.com/css2?family=Montserrat:wght@400;500;600;700&family=Nunito:wght@600;700;800&display=swap">
<style>
:root{
  --teal:#17a9ab;
  --teal-dark:#0e8487;
  --teal-soft:#e6f5f2;
  --teal-band:#49c0c6;
  --ink:#1d2a2f;
  --muted:#5b6a70;
  --white:#ffffff;
  --footer:#f1f3f3;
  --water-1:#3fb6d8;
  --water-2:#1a7fa8;
}
*{box-sizing:border-box;margin:0;padding:0}
html,body{width:1200px;height:3852px;overflow:hidden}
body{position:relative;background:var(--white);font-family:'Montserrat',sans-serif;color:var(--ink)}
.abs{position:absolute}
h1,h2,h3{font-family:'Nunito',sans-serif;font-weight:800;color:var(--ink)}
.eyebrow{font-size:16px;font-weight:600;color:var(--teal)}
.btn{display:inline-block;background:var(--teal);color:var(--white);font-size:14px;font-weight:600;padding:12px 28px;border-radius:2px}
.photo{background:linear-gradient(135deg,var(--water-1),var(--water-2))}

/* header & hero */
.hero{left:0;top:0;width:1200px;height:740px;background:linear-gradient(160deg,#5f8a68 0%,#7fb0b8 30%,#2ea6d0 60%,#166f97 100%)}
.nav{left:0;top:0;width:1200px;height:64px;display:flex;align-items:center;padding:0 80px}
.brand{display:flex;align-items:center;gap:10px;font-family:'Nunito',sans-serif;font-weight:700;font-size:26px;color:var(--white)}
.brand-dot{width:30px;height:30px;border-radius:50%;background:var(--white)}
.nav-links{margin-left:auto;display:flex;gap:38px;align-items:center;font-size:14px;color:var(--white);font-weight:500}
.nav-links .btn{padding:10px 22px}
.hero-card{left:112px;top:368px;width:450px;height:256px;background:var(--white);padding:24px 30px}
.hero-card h1{font-size:46px;line-height:1.05}
.hero-card p{font-size:12px;line-height:1.5;color:var(--muted);margin:12px 0 16px;width:320px}
.scroll-cue{left:560px;top:692px;width:80px;height:80px;border-radius:50%;background:var(--white);display:flex;align-items:center;justify-content:center}
.scroll-cue span{width:52px;height:52px;border-radius:50%;background:var(--teal);display:flex;align-items:center;justify-content:center}

/* about */
.about{left:72px;top:860px;width:1056px;height:520px;background:var(--teal-soft);text-align:center;padding-top:56px}
.about h2{font-size:34px;margin-top:6px}
.about-illus{width:130px;height:70px;margin:22px auto 0;background:#8fd0e6}
.about p{font-size:19px;line-height:1.55;color:var(--muted);width:840px;margin:34px auto 26px}

/* services */
.wash{left:0;top:1680px;width:1200px;height:330px;background:linear-gradient(180deg,rgba(73,192,198,0) 0%,var(--teal-band) 25%,var(--teal-band) 70%,rgba(73,192,198,0) 100%)}
.service-intro{left:72px;top:1490px;width:268px;height:290px;background:var(--white);padding:22px 20px;box-shadow:0 6px 18px rgba(0,0,0,.08)}
.service-intro h2{font-size:26px;line-height:1.15;margin:4px 0 16px}
.service-intro .photo{height:110px}
.service-card{top:1488px;width:176px;height:300px;background:var(--white);box-shadow:0 6px 18px rgba(0,0,0,.08)}
.service-card .photo{height:248px}
.service-card p{font-size:13px;font-weight:600;text-align:center;line-height:52px}
.services-btn{left:496px;top:1840px;background:var(--ink);color:var(--white);font-size:14px;font-weight:600;padding:13px 32px}

/* why */
.why-photo{left:168px;top:2130px;width:424px;height:318px;background:linear-gradient(135deg,#6fa57a,#3fb6d8 55%,#1f85b0)}
.why{left:648px;top:2160px;width:480px}
.why h2{font-size:44px;line-height:1.08;margin:6px 0 18px}
.why ul{list-style:none}
.why li{display:flex;gap:10px;align-items:center;font-size:14px;color:var(--muted);margin-bottom:12px}
.tick{width:16px;height:16px;border-radius:3px;background:var(--teal);flex:none}

/* gallery */
.gallery-head{left:0;top:2526px;width:1200px;text-align:center}
.gallery-head h2{font-size:40px;line-height:1.1;margin-top:4px}
.gallery-btn{left:520px;top:3048px}

/* contact */
.contact{left:0;top:3180px;width:1200px;text-align:center}
.contact h2{font-size:40px;margin:8px 0 18px}
.contact p{font-size:13px;line-height:1.6;color:var(--muted);width:560px;margin:0 auto 18px}

/* footer */
.footer{left:0;top:3456px;width:1200px;height:344px;background:var(--footer)}
.footer .brand{color:var(--ink);font-size:30px;position:absolute;left:80px;top:130px}
.footer .brand-dot{background:var(--teal)}
.f-col{top:60px}
.f-col h3{font-size:20px;margin-bottom:14px}
.f-col li{list-style:none;font-size:13px;color:var(--muted);line-height:22px}
.news input{display:block;width:224px;height:36px;border:1px solid #d5dcdc;background:var(--white);font:12px 'Montserrat',sans-serif;padding:0 12px;color:var(--muted);margin:16px 0 8px}
.news .btn{width:224px;text-align:center}
.bottom-bar{left:0;top:3800px;width:1200px;height:52px;background:var(--teal);color:var(--white);font-size:13px;text-align:center;line-height:52px}
.chat{left:1096px;top:3766px;width:60px;height:60px;border-radius:50%;background:#111;display:flex;align-items:center;justify-content:center}
</style>
</head>
<body>

<section class="abs hero" role="img" aria-label="Luxury poolside terrace with loungers, umbrellas and palm trees around a blue pool"></section>
<header class="abs nav">
  <div class="brand"><span class="brand-dot"></span>Coral Basins</div>
  <nav class="nav-links"><span>Home</span><span>About Us</span><span>Service</span><span>Why Choose Us</span><span>Gallery</span><span class="btn">Contact Us</span></nav>
</header>
<div class="abs hero-card">
  <h1>Crafting Luxury<br>Pools</h1>
  <p>Transform your outdoor space with custom-designed pools that define elegance and sophistication.</p>
  <span class="btn">Get Your Free Consultation</span>
</div>
<div class="abs scroll-cue"><span><svg width="22" height="22" viewBox="0 0 22 22" fill="none" stroke="#fff" stroke-width="2.4" stroke-linecap="round"><path d="M11 3v15M5 12l6 6 6-6"/></svg></span></div>

<section class="abs about">
  <div class="eyebrow">About Us</div>
  <h2>Crafting Premium Pool Experiences</h2>
  <div class="about-illus" role="img" aria-label="Small illustration of a swimming pool"></div>
  <p>"At Coral Basins, we specialize in designing and building luxury swimming pools that combine aesthetic beauty with exceptional functionality. From modern infinity pools to timeless classic designs, we create outdoor sanctuaries tailored to your lifestyle."</p>
  <span class="btn">Learn More</span>
</section>

<div class="abs wash" role="img" aria-label="Turquoise watercolor background band"></div>
<div class="abs service-intro">
  <div class="eyebrow">Service</div>
  <h2>Bespoke Pool Solutions for Every Vision</h2>
  <div class="photo" role="img" aria-label="Aerial view of a rounded pool"></div>
</div>
<div class="abs service-card" style="left:352px"><div class="photo" role="img" aria-label="Custom designed pool with tiled steps"></div><p>Custom Pool Design</p></div>
<div class="abs service-card" style="left:546px"><div class="photo" role="img" aria-label="Pool under construction" style="background:linear-gradient(135deg,#9fd6e6,#3aa7cf)"></div><p>Pool Construction</p></div>
<div class="abs service-card" style="left:740px"><div class="photo" role="img" aria-label="Technician cleaning a pool" style="background:linear-gradient(160deg,#7c8f86,#2c8fb8)"></div><p>Maintenance</p></div>
<div class="abs service-card" style="left:934px"><div class="photo" role="img" aria-label="Pool loungers and accessories" style="background:linear-gradient(135deg,#e8eef0,#4fb9d9)"></div><p>Luxury Accessories</p></div>
<div class="abs services-btn">Discover Our Services</div>

<div class="abs why-photo" role="img" aria-label="Collage of resort pools surrounded by gardens"></div>
<section class="abs why">
  <div class="eyebrow">Why Choose Us</div>
  <h2>Unmatched Quality.<br>Exceptional.</h2>
  <ul>
    <li><span class="tick"></span>Expert designers and builders with years of experience.</li>
    <li><span class="tick"></span>Attention to detail in every project.</li>
    <li><span class="tick"></span>Materials and finishes that ensure durability and elegance.</li>
    <li><span class="tick"></span>A seamless, stress-free pool-building experience.</li>
  </ul>
  <span class="btn" style="margin-top:8px">Read More</span>
</section>

<section class="abs gallery-head">
  <div class="eyebrow">Gallery</div>
  <h2>Pools That Inspire</h2>
</section>
<div class="abs photo" style="left:200px;top:2632px;width:200px;height:170px" role="img" aria-label="Rectangular pool at a villa"></div>
<div class="abs photo" style="left:200px;top:2816px;width:200px;height:190px;background:linear-gradient(135deg,#4cc3e6,#1678a6)" role="img" aria-label="Pool with wooden deck"></div>
<div class="abs photo" style="left:472px;top:2632px;width:256px;height:264px;background:linear-gradient(160deg,#6b9c6f,#2fb0d8 55%,#176f9a)" role="img" aria-label="Resort pool lined with palm trees"></div>
<div class="abs photo" style="left:472px;top:2908px;width:256px;height:100px;background:linear-gradient(135deg,#9fc7d8,#2a8fbd)" role="img" aria-label="Long lap pool at dusk"></div>
<div class="abs photo" style="left:800px;top:2632px;width:200px;height:170px;background:linear-gradient(160deg,#7bb08a,#35b2dc)" role="img" aria-label="Curved pool with loungers"></div>
<div class="abs photo" style="left:800px;top:2816px;width:200px;height:190px;background:linear-gradient(135deg,#56c0e4,#0f6f9d)" role="img" aria-label="Modern pool beside a white house"></div>
<span class="abs btn gallery-btn">View Our Gallery</span>

<section class="abs contact">
  <div class="eyebrow">Contact</div>
  <h2>Start Your Luxury Pool Journey Today</h2>
  <p>Our team is ready to bring your dream pool to life. Schedule a consultation and take the first step towards a premium pool experience.</p>
  <span class="btn">Book a Consultation</span>
</section>

<footer class="abs footer">
  <div class="brand"><span class="brand-dot"></span>Coral Basins</div>
  <div class="abs f-col" style="left:376px"><h3>Company</h3><ul><li>Home</li><li>Features</li><li>About Us</li><li>Services</li><li>Blog</li><li>Contact</li></ul></div>
  <div class="abs f-col" style="left:540px"><h3>Custom</h3><ul><li>Blog</li><li>Shipping</li><li>Login</li><li>Register</li><li>Terms of Service</li><li>Reviews</li></ul></div>
  <div class="abs f-col" style="left:700px"><h3>Contact Us</h3><ul><li>Phone</li><li>(555) 014-2290</li><li>Hours</li><li>Mon-Fri 9am–6pm</li><li>Email</li><li>hello@coralbasins.com</li></ul></div>
  <div class="abs f-col news" style="left:904px"><h3>Signup Newsletter</h3><ul><li>Sign up to get the latest on sales,</li><li>new releases and more.</li></ul><input value="Enter email address" aria-label="Email"><span class="btn">Submit</span></div>
</footer>
<div class="abs bottom-bar">© Copyright 2025 Coral Basins All Rights Reserved</div>
<div class="abs chat"><svg width="28" height="26" viewBox="0 0 28 26"><path d="M4 3h20a2 2 0 0 1 2 2v12a2 2 0 0 1-2 2H12l-6 5v-5H4a2 2 0 0 1-2-2V5a2 2 0 0 1 2-2z" fill="#fff"/></svg></div>

</body>
</html>
```